Business Cards for 4 people

We need to update our current business cards for 4 of our employees and make some minor design changes. Mostly have to update the information on the cards with a new address and titles.

```html
<!DOCTYPE html>
<html lang="en">
<head>
<meta charset="UTF-8">
<title>Brightridge Partners – Business Cards</title>
<link href="https://fonts.googleapis.com/css2?family=Poppins:wght@400;500;600&display=swap" rel="stylesheet">
<style>
  :root {
    --navy: #22305f;
    --green: #009345;
    --white: #ffffff;
    --stage: #ecebed;
    --ink: #3a3d4a;
  }
  * { box-sizing: border-box; margin: 0; padding: 0; }
  html, body { width: 1200px; height: 1200px; overflow: hidden; }
  body {
    background: var(--stage);
    font-family: "Poppins", Arial, sans-serif;
    position: relative;
  }
  .card {
    position: absolute;
    left: 180px;
    width: 840px;
    height: 480px;
    background: var(--white);
    overflow: hidden;
    box-shadow: 0 10px 30px rgba(0,0,0,0.12);
  }
  .card-front { top: 90px; }
  .card-back { top: 630px; }

  /* Front */
  .front-brand {
    position: absolute;
    top: 120px;
    left: 0;
    width: 100%;
    display: flex;
    align-items: center;
    justify-content: center;
    gap: 18px;
  }
  .brand-mark {
    width: 34px;
    height: 34px;
    background: var(--green);
  }
  .brand-name {
    color: var(--green);
    font-weight: 600;
    font-size: 46px;
    letter-spacing: 1px;
  }
  .front-band {
    position: absolute;
    left: 0;
    bottom: 0;
    width: 100%;
    height: 120px;
    background: var(--green);
    display: flex;
    align-items: center;
    justify-content: center;
  }
  .tagline {
    color: var(--white);
    font-size: 30px;
    font-weight: 400;
    letter-spacing: 1px;
  }

  /* Back */
  .back-shapes { position: absolute; inset: 0; }
  .back-brand {
    position: absolute;
    left: 34px;
    top: 140px;
    width: 300px;
  }
  .back-brand .brand-row { display: flex; align-items: center; gap: 10px; }
  .back-brand .brand-mark { width: 20px; height: 20px; }
  .back-brand .brand-name { font-size: 25px; letter-spacing: 0.5px; }
  .back-brand .sub-tagline {
    color: var(--white);
    font-size: 18px;
    margin-top: 10px;
    padding-left: 30px;
  }
  .contact {
    position: absolute;
    left: 440px;
    top: 62px;
    width: 380px;
    color: var(--ink);
  }
  .person-name {
    color: var(--navy);
    font-size: 42px;
    font-weight: 500;
    line-height: 1.1;
  }
  .person-title {
    color: var(--green);
    font-size: 15px;
    font-weight: 500;
    margin-top: 2px;
    margin-bottom: 26px;
  }
  .contact-list { list-style: none; }
  .contact-list li {
    display: flex;
    align-items: center;
    gap: 12px;
    font-size: 17px;
    line-height: 1.25;
    margin-bottom: 8px;
  }
  .contact-list .icon { width: 16px; height: 16px; flex: none; fill: var(--navy); }
  .contact-list .accent { color: var(--green); }
  .contact-list li.address { align-items: flex-start; margin-top: 18px; }
  .contact-list li.address .icon { margin-top: 3px; }
</style>
</head>
<body>

  <section class="card card-front">
    <div class="front-brand">
      <span class="brand-name">Brightridge Partners</span>
      <span class="brand-mark"></span>
    </div>
    <div class="front-band">
      <span class="tagline">THE FUTURE OF INVESTING</span>
    </div>
  </section>

  <section class="card card-back">
    <svg class="back-shapes" width="840" height="480" viewBox="0 0 840 480">
      <polygon points="0,0 360,0 218,480 0,480" fill="#22305f"/>
      <polygon points="382,0 394,0 300,480 240,480" fill="#009345"/>
    </svg>
    <div class="back-brand">
      <div class="brand-row">
        <span class="brand-name">Brightridge Partners</span>
        <span class="brand-mark"></span>
      </div>
      <p class="sub-tagline">The Future of Investing</p>
    </div>
    <div class="contact">
      <h1 class="person-name">Dana Whitlock</h1>
      <p class="person-title">Investor Relations</p>
      <ul class="contact-list">
        <li>
          <svg class="icon" viewBox="0 0 16 16"><path d="M3 1h3l1.5 4-2 1.2a9 9 0 0 0 4.3 4.3L11 8.5l4 1.5v3a2 2 0 0 1-2 2A12 12 0 0 1 1 3a2 2 0 0 1 2-2z"/></svg>
          555-310-4826
        </li>
        <li>
          <svg class="icon" viewBox="0 0 16 16"><path d="M4 0h8a1 1 0 0 1 1 1v14a1 1 0 0 1-1 1H4a1 1 0 0 1-1-1V1a1 1 0 0 1 1-1zm1 2v10h6V2zm3 11a1 1 0 1 0 0 2 1 1 0 0 0 0-2z"/></svg>
          555-740-1193
        </li>
        <li>
          <svg class="icon" viewBox="0 0 16 16"><path d="M1 3h14v10H1zm1.5 1.2V5l5.5 4 5.5-4v-.8z"/></svg>
          <span>dwhitlock@<span class="accent">brightridge</span>.co</span>
        </li>
        <li>
          <svg class="icon" viewBox="0 0 16 16"><circle cx="8" cy="8" r="7" fill="none" stroke="#22305f" stroke-width="1.6"/><path d="M1 8h14M8 1c3 3 3 11 0 14M8 1c-3 3-3 11 0 14" fill="none" stroke="#22305f" stroke-width="1.4"/></svg>
          <span>www.<span class="accent">brightridge</span>.co</span>
        </li>
        <li class="address">
          <svg class="icon" viewBox="0 0 16 16"><path d="M8 0a5.5 5.5 0 0 1 5.5 5.5C13.5 10 8 16 8 16S2.5 10 2.5 5.5A5.5 5.5 0 0 1 8 0zm0 3.5a2 2 0 1 0 0 4 2 2 0 0 0 0-4z"/></svg>
          <span>412 Harbor Rd. Suite #210,<br>Seaview, FL 32000</span>
        </li>
      </ul>
    </div>
  </section>

</body>
</html>
```